Asphalt Driveway Billboard Design

We need a billboard designed for an Asphalt & Concrete Company in Minnesota. We want to advertise Asphalt Driveways on this billboard! Logo is uploaded below. Our website is pinecrest-paving.net for more information.

```html
<!DOCTYPE html>
<html lang="en">
<head>
<meta charset="utf-8">
<title>Pinecrest Paving – Asphalt Driveway Billboard</title>
<link rel="stylesheet" href="https://fonts.googleapis.com/css2?family=Montserrat:wght@700;800&display=swap">
<style>
  :root {
    --backdrop: #00003f;
    --paper: #ffffff;
    --brand-blue: #0b5aa6;
    --deep-navy: #0a3566;
    --accent-gold: #fbab0c;
    --photo-dark: #2f3032;
    --photo-mid: #4b4c4f;
    --text-light: #ffffff;
  }
  html, body {
    margin: 0;
    padding: 0;
    width: 1137px;
    height: 1200px;
    overflow: hidden;
    background: var(--backdrop);
    font-family: "Montserrat", "Helvetica Neue", Arial, sans-serif;
  }
  .canvas {
    position: relative;
    width: 1137px;
    height: 1200px;
  }
  .billboard {
    position: absolute;
    left: 38px;
    top: 362px;
    width: 1060px;
    height: 475px;
    background: var(--paper);
    overflow: hidden;
  }
  .billboard h1, .billboard h2, .billboard p, .billboard li {
    white-space: nowrap;
  }
  .info-band {
    position: absolute;
    left: 0;
    top: 205px;
    width: 100%;
    height: 156px;
    background: var(--brand-blue);
  }
  .contact-bar {
    position: absolute;
    left: 0;
    top: 424px;
    width: 100%;
    height: 51px;
    background: var(--brand-blue);
  }
  .headline {
    position: absolute;
    left: 56px;
    top: 82px;
    margin: 0;
    font-weight: 800;
    font-size: 29px;
    line-height: 40px;
    color: var(--accent-gold);
    text-transform: uppercase;
  }
  .benefits {
    position: absolute;
    left: 50px;
    top: 242px;
    margin: 0;
    padding: 0;
    list-style: none;
    font-weight: 700;
    font-size: 16.5px;
    line-height: 23px;
    color: var(--text-light);
    text-transform: uppercase;
  }
  .benefits li::before {
    content: "▪";
    font-size: 9px;
    margin-right: 6px;
    vertical-align: 3px;
  }
  .web-address, .phone-line {
    position: absolute;
    top: 437px;
    margin: 0;
    font-weight: 700;
    font-size: 17.5px;
    line-height: 24px;
    color: var(--text-light);
    text-transform: uppercase;
  }
  .web-address { left: 42px; }
  .phone-line { left: 337px; }
  .phone-number { color: var(--accent-gold); }
  .hero-art {
    position: absolute;
    left: 0;
    top: 0;
    width: 1060px;
    height: 475px;
  }
  .brand-name {
    position: absolute;
    left: 640px;
    width: 320px;
    top: 146px;
    margin: 0;
    text-align: center;
    font-weight: 700;
    font-size: 24px;
    letter-spacing: 1px;
    color: var(--text-light);
  }
  .service-title {
    position: absolute;
    left: 575px;
    width: 480px;
    top: 232px;
    margin: 0;
    text-align: center;
    font-weight: 800;
    font-size: 40px;
    line-height: 48px;
    letter-spacing: -0.5px;
    color: var(--accent-gold);
    text-transform: uppercase;
  }
  .service-subtitle {
    position: absolute;
    left: 575px;
    width: 480px;
    top: 284px;
    margin: 0;
    text-align: center;
    font-weight: 700;
    font-size: 19px;
    line-height: 26px;
    color: var(--text-light);
    text-transform: uppercase;
  }
</style>
</head>
<body>
<div class="canvas">
  <section class="billboard">
    <div class="info-band"></div>
    <div class="contact-bar"></div>

    <h1 class="headline">Upgrade your driveway<br>with peace of mind</h1>

    <ul class="benefits">
      <li>Replace your driveway with confidence.</li>
      <li>Our warranty covers your investment</li>
      <li>for 3 years with proper maintenance.</li>
      <li>Call us for a free estimate!</li>
    </ul>

    <p class="web-address">pinecrest-paving.net</p>
    <p class="phone-line">Call us: <span class="phone-number">555-014-2286</span></p>

    <svg class="hero-art" viewBox="0 0 1060 475">
      <defs>
        <linearGradient id="houseTone" x1="0" y1="0" x2="0" y2="1">
          <stop offset="0" stop-color="#3c3d40"/>
          <stop offset="0.55" stop-color="#4b4c4f"/>
          <stop offset="0.7" stop-color="#3a3b3d"/>
          <stop offset="1" stop-color="#2f3032"/>
        </linearGradient>
      </defs>
      <path class="swoosh-outer" d="M548 0 C498 110 500 300 638 475 L1060 475 L1060 0 Z" fill="#0b5aa6"/>
      <path class="swoosh-inner" d="M578 0 C530 110 532 300 660 475 L1060 475 L1060 0 Z" fill="#0a3566"/>
      <path class="house-photo" role="img" aria-label="Photo of a grey two-storey house with a freshly paved asphalt driveway"
            d="M588 0 C541 110 544 300 672 475 L1060 475 L1060 0 Z" fill="url(#houseTone)"/>
    </svg>

    <p class="brand-name">PINECREST</p>
    <h2 class="service-title">Asphalt Driveway</h2>
    <p class="service-subtitle">Replacement with a warranty!</p>
  </section>
</div>
</body>
</html>
```